Forex website redesign

We need an attractive good looking website design that increase the apatite of our visitors to subscribe to our advisory service, beside the fact that we do offer very high quality service.

Our service is where we connect to investor accounts who are subscribed, to automatically deliver and execute our advise to buy or sell straight onto their account using high tech software.

The final design should communicate financial safty and growth.
Updates

Here is something to keep in mind about our business model that may help you in your design, we SHOW people the right way to invest, so they can make money instead of going somewere else and lose it. Beside that point, most websites in forex that includes pictures of happy and excited people who make money ALWAY turn out to be scam. So please try not to position our business that way in visitor first impression once he/she visit our site.

Thank you for your help :)

Target Market(s)

Financial Market, 20-70 years old

Industry/Entity Type

Financial

Requirements
Must have
• Call to action feature + Logo redesign. Please visit www.brelvantrade.net to get an idea of how we want it. Also include the personal photos of our advisors in your deign.

```html
<!DOCTYPE html>
<html lang="en">
<head>
<meta charset="utf-8">
<title>Brelvan Trade Ltd</title>
<link href="https://fonts.googleapis.com/css2?family=Roboto:ital,wght@0,300;0,400;0,500;0,700;1,300;1,700&display=swap" rel="stylesheet">
<style>
:root{
  --navy:#1f3a66;
  --navy-dark:#1a2f52;
  --bg:#dcdde0;
  --white:#ffffff;
  --ink:#3b3b3b;
  --muted:#8a8a8a;
  --link:#1f3a66;
  --orange:#f4511e;
  --footer:#2b2b2b;
  --footer-bottom:#1f1f1f;
  --footer-text:#d8d8d8;
}
*{box-sizing:border-box;margin:0;padding:0}
html,body{width:847px;height:1200px;overflow:hidden}
body{background:var(--bg);font-family:'Roboto',sans-serif;color:var(--ink);position:relative}
.topbar{position:absolute;left:0;top:0;width:847px;height:9px;background:var(--navy-dark)}
.brand{position:absolute;left:96px;top:38px;display:flex;align-items:center;gap:8px}
.brand-mark{width:24px;height:24px;background:var(--navy)}
.brand-name{font-size:24px;font-weight:700;color:var(--navy);line-height:1}
.brand-tag{font-size:10px;font-weight:700;font-style:italic;color:var(--navy);margin-top:3px}
.contact-mail{position:absolute;right:92px;top:38px;font-size:12px;color:var(--ink);font-weight:300}
.search{position:absolute;right:92px;top:57px;width:166px;height:17px;display:flex}
.search input{flex:1;border:none;background:#fff;font:300 8px 'Roboto',sans-serif;padding-left:9px;color:#999}
.search button{width:22px;border:none;background:var(--navy);display:flex;align-items:center;justify-content:center}
.nav{position:absolute;left:92px;top:92px;width:664px;height:38px;background:var(--navy);display:flex;align-items:center;padding-left:18px;gap:21px}
.nav a{color:#fff;text-decoration:none;font-size:12px;font-weight:300}
.hero{position:absolute;left:92px;top:130px;width:664px;height:267px;background:linear-gradient(90deg,#cfd0d3,#e6e6e8 60%,#d2d3d6)}
.hero-photo{position:absolute;left:0;top:0;width:314px;height:267px;background:linear-gradient(180deg,#c8cacd,#7c8086 55%,#2a2f3a)}
.hero-title{position:absolute;left:342px;top:88px;font-size:25px;font-weight:300;color:var(--navy)}
.hero-text{position:absolute;left:342px;top:124px;width:270px;font-size:9px;line-height:17px;font-weight:300;color:#666}
.hero-text a,.card-text a{color:var(--link);text-decoration:none;font-weight:400}
.hero-arrows{position:absolute;left:592px;top:234px;display:flex;gap:6px}
.cta{position:absolute;left:92px;top:407px;width:664px;height:49px;background:var(--navy);display:flex;align-items:center;justify-content:space-between;padding:0 22px;box-shadow:0 12px 10px -8px rgba(0,0,0,.45)}
.cta-text{color:#fff;font-size:17px;font-weight:300}
.cta-button{background:var(--orange);color:#fff;font-size:11px;font-weight:700;padding:8px 17px;border-radius:2px}
.welcome-title{position:absolute;left:0;width:847px;top:486px;text-align:center;font-size:18px;font-weight:300;color:var(--navy)}
.welcome-text{position:absolute;left:92px;width:664px;top:516px;text-align:center;font-size:9px;line-height:17px;font-weight:300;color:#333}
.col-title{position:absolute;top:569px;font-size:13px;font-weight:300;color:#444}
.card{position:absolute;top:592px;width:212px;height:269px;background:#fff;box-shadow:2px 4px 6px rgba(0,0,0,.2)}
.card-image{position:absolute;left:14px;top:17px;width:183px;height:114px}
.card-text{position:absolute;left:19px;top:150px;width:180px;font-size:9px;line-height:17px;font-weight:300;color:#888}
.card-text.justify{text-align:justify}
.caption{position:absolute;left:0;bottom:0;width:183px;height:30px;background:rgba(31,58,102,.75);color:#fff;font-size:11px;font-weight:300;display:flex;align-items:center;padding-left:11px}
.partners-band{position:absolute;left:0;top:896px;width:847px;height:78px;background:#fff}
.quote{position:absolute;left:100px;top:18px;width:305px;text-align:center;font-size:9px;line-height:17px;font-style:italic;font-weight:300;color:#555}
.quote-author{display:block;font-style:normal;font-size:12px;font-weight:400;color:#333;margin-top:2px}
.divider{position:absolute;left:418px;top:12px;width:1px;height:54px;background:#e5e5e5}
.partners{position:absolute;left:434px;top:26px;width:320px;display:flex;justify-content:space-between;align-items:center;font-size:10px;font-weight:500;color:#777}
.footer{position:absolute;left:0;top:974px;width:847px;height:188px;background:var(--footer);color:var(--footer-text)}
.footer h4{font-size:10px;font-weight:400;color:#fff;margin-bottom:13px}
.footer-col{position:absolute;top:24px;font-size:8px;font-weight:300}
.footer-col li{list-style:none;line-height:17px}
.signup p{line-height:14px;margin-bottom:8px;width:160px}
.signup input{display:block;width:157px;height:19px;border:none;font:300 8px 'Roboto',sans-serif;padding-left:10px;margin-bottom:10px;color:#999}
.subscribe{margin-left:88px;width:69px;height:17px;border-radius:9px;background:var(--orange);color:#fff;font-size:9px;font-weight:500;display:flex;align-items:center;justify-content:center}
.social li{display:flex;align-items:center;justify-content:space-between;width:96px;margin-bottom:9px}
.social span.dot{width:19px;height:19px;border-radius:50%;background:#fff}
.copyright{position:absolute;left:0;top:1162px;width:847px;height:38px;background:var(--footer-bottom);color:var(--footer-text);font-size:8px;font-weight:300;text-align:center;line-height:38px}
</style>
</head>
<body>
<div class="topbar"></div>

<header>
  <div class="brand">
    <div class="brand-mark"></div>
    <div>
      <div class="brand-name">Brelvan Trade Ltd</div>
      <div class="brand-tag">From Traders to Traders, THE REAL DEAL</div>
    </div>
  </div>
  <div class="contact-mail">support@brelvantrade.net</div>
  <div class="search">
    <input type="text" value="Search" aria-label="Search">
    <button aria-label="Search"><svg width="10" height="10" viewBox="0 0 10 10"><circle cx="4" cy="4" r="3" fill="none" stroke="#fff" stroke-width="1.4"/><line x1="6.2" y1="6.2" x2="9" y2="9" stroke="#fff" stroke-width="1.6"/></svg></button>
  </div>
</header>

<nav class="nav">
  <a href="#">Home</a><a href="#">About Us</a><a href="#">Order</a><a href="#">Performance</a><a href="#">Chen Haoran Special</a><a href="#">Terms &amp; Conditions</a><a href="#">Why Us?</a><a href="#">Contact Us</a>
</nav>

<section class="hero">
  <div class="hero-photo" role="img" aria-label="Portrait photo of trader Chen Haoran in a suit beside a trading monitor"></div>
  <h1 class="hero-title">brelvantrade safe player</h1>
  <p class="hero-text">Another member in our elite club 0 mr chen haoran. a very talented trader who has been managing accounts with total value of many million dollars...<a href="#">Read More</a></p>
  <div class="hero-arrows">
    <svg width="24" height="24" viewBox="0 0 24 24"><circle cx="12" cy="12" r="12" fill="#333"/><polyline points="14,7 9,12 14,17" fill="none" stroke="#fff" stroke-width="2.4"/></svg>
    <svg width="24" height="24" viewBox="0 0 24 24"><circle cx="12" cy="12" r="12" fill="#eee"/><polyline points="10,7 15,12 10,17" fill="none" stroke="#bbb" stroke-width="2.4"/></svg>
  </div>
</section>

<section class="cta">
  <span class="cta-text">LET US DO THE PICK ,WHILE YOU ENJOY THE RIDE</span>
  <span class="cta-button">ORDER NOW</span>
</section>

<h2 class="welcome-title">Welcome to Brelvan Trade Ltd</h2>
<p class="welcome-text">Brelvan Trade Ltd is the ONLY forex signal service on this planet that provides full info about the traders involved including REAL personal photos, REAL personal details and portfolios, as well as YEARS of verified and consistent live trading performance.</p>

<h3 class="col-title" style="left:95px">How Signals Work</h3>
<h3 class="col-title" style="left:317px">Performance</h3>
<h3 class="col-title" style="left:544px">Why You Choose Us ?</h3>

<article class="card" style="left:92px">
  <div class="card-image" role="img" aria-label="Illustration of a hand releasing floating digital screens" style="background:radial-gradient(circle at 55% 40%,#8a7a6a,#3a3c44 60%,#1e2026)"></div>
  <p class="card-text">Once you subscribe, you will be re-directed to a secure page to download and set-up the EA copier on your VPS with all the instructions you need(We provide full support, and we can set it up for you for no additional charge...<a href="#">Read More</a></p>
</article>

<article class="card" style="left:318px">
  <div class="card-image" role="img" aria-label="Photo of master trader seated beside a chart monitor" style="background:linear-gradient(90deg,#bfc1c3,#d7d7d5 50%,#a9acb0)">
    <div class="caption">brelvantrade Master
      <svg width="32" height="14" viewBox="0 0 32 14" style="margin-left:14px"><circle cx="7" cy="7" r="6.5" fill="#888"/><polyline points="8,4 5,7 8,10" fill="none" stroke="#ddd" stroke-width="1.4"/><circle cx="24" cy="7" r="6.5" fill="#eee"/><polyline points="23,4 26,7 23,10" fill="none" stroke="#333" stroke-width="1.4"/></svg>
    </div>
  </div>
  <p class="card-text">Our Master trader is the head of our Elite group traders and has a 5 years of solid real live trading performance to show-off with. Mr. Marek Dovan is an NFA Exempt CTA, NFA ID is: 0519832...<a href="#">Read More</a></p>
</article>

<article class="card" style="left:545px">
  <div class="card-image" role="img" aria-label="Photo of a team of business professionals" style="background:linear-gradient(180deg,#e8e8e8,#9a8a80 45%,#2c3140)"></div>
  <p class="card-text justify">We stand out from our competition because we can pick &amp; hire winning systems while most others can't. Many big signal businesses out there such as Tradevane...<a href="#">Read More</a></p>
</article>

<section class="partners-band">
  <p class="quote">"Neque porro quisquam est qui dolorem ipsum quia dolor sit amet, consectetur, adipisci velit..."<span class="quote-author">By, Laura Pimsby</span></p>
  <div class="divider"></div>
  <div class="partners"><span>Northgate</span><span>Veloria</span><span>Quillo</span><span>Ardent</span><span>Solvane Group</span></div>
</section>

<footer class="footer">
  <div class="footer-col" style="left:91px">
    <h4>Quick Links</h4>
    <ul><li>Home</li><li>About Us</li><li>Order</li><li>Performance</li><li>Chen Haoran Special</li><li>Terms &amp; Conditions</li><li>Why Us?</li><li>Contact Us</li></ul>
  </div>
  <div class="footer-col" style="left:261px">
    <h4>Support Links</h4>
    <ul><li>Legal Notice</li><li>Privacy Policy</li><li>Terms &amp; Conditions</li><li>Help</li></ul>
  </div>
  <div class="footer-col signup" style="left:432px">
    <h4>Newsletter SignUp</h4>
    <p>Sign-up for our daily emails by entering your information below:</p>
    <input type="text" value="Name" aria-label="Name">
    <input type="text" value="Enter Your E-Mail ID" aria-label="Email">
    <div class="subscribe">Subscribe</div>
  </div>
  <div class="footer-col social" style="left:657px">
    <h4>Connect With Us</h4>
    <ul><li><span class="dot"></span>Chirpline</li><li><span class="dot"></span>Facenote</li><li><span class="dot"></span>Linkwork</li></ul>
  </div>
</footer>
<div class="copyright">Copyright ©2013 Company Name &nbsp; - All rights reserved</div>
</body>
</html>
```